New business card for KT4 Linkway, a marketing company.

We need a new business card design. We would like it to be blue gray and white. We would like some movement but in a more subtle pattern than in the file we uploaded. We are a marketing company that connects brands with their target audiences - we make connections. We work in the New York Metro area with sophisticated clients. The card should feel modern, upscale and professional.

Target Market(s)

Businesses looking to grow their brands in tourism and nightlife. We work with liquor and beer companies and with Tourism bureaus and companies.

Industry/Entity Type

Marketing

Contact Information for Business Card

Would like a horizontal layout, two-sided. Would like the logo on the back with the tagline ' "bringing each brand closer to the right crowd" under the logo. On the front, we would like name, title, contact email, contact phone, website.

Font styles to use
Sans Serif

Colors
3377b5
85cae6
ffffff

Requirements
Must have
• Our logo. See attached. Otherwise, open to your ideas.
Should not have
• No colors we don't want - no reds/pinks/oranges please

```html
<!DOCTYPE html>
<html lang="en">
<head>
<meta charset="utf-8">
<title>KT4 Linkway Business Card</title>
<link href="https://fonts.googleapis.com/css2?family=Montserrat:wght@300;400&family=Oswald:wght@400;600&display=swap" rel="stylesheet">
<style>
  :root{
    --bg:#1d1d1e;
    --paper:#f6f6f5;
    --ink-gray:#8c8c8c;
    --ink-soft:#a3a3a3;
    --blue-deep:#3377b5;
    --blue-light:#85cae6;
    --white:#ffffff;
  }
  *{margin:0;padding:0;box-sizing:border-box}
  html,body{width:941px;height:1200px;overflow:hidden;background:var(--bg)}
  .canvas{position:relative;width:941px;height:1200px}
  .card{position:absolute;left:190px;width:560px;height:320px;border-radius:22px;overflow:hidden;background:var(--paper);box-shadow:0 10px 30px rgba(0,0,0,.45)}
  .card--back{top:150px}
  .card--front{top:730px}
  .card__art{position:absolute;inset:0;width:100%;height:100%}
  .brand{position:absolute;font-family:'Montserrat',sans-serif;font-weight:400;color:var(--ink-gray);letter-spacing:.06em;white-space:nowrap}
  .card--back .brand{left:0;right:0;top:92px;text-align:center;font-size:30px}
  .tagline{position:absolute;left:0;right:0;top:146px;text-align:center;font-family:'Montserrat',sans-serif;font-weight:300;font-size:13.5px;color:var(--ink-soft);letter-spacing:.03em}
  .card--front .brand{left:28px;top:30px;font-size:14px}
  .person{position:absolute;right:290px;top:100px;text-align:right;font-family:'Oswald',sans-serif;color:var(--ink-gray)}
  .person__name{font-weight:600;font-size:23px;letter-spacing:.12em}
  .person__title{font-weight:400;font-size:14px;letter-spacing:.14em}
  .divider{position:absolute;left:284px;top:92px;width:5px;height:80px;border-radius:3px;background:var(--blue-light)}
  .contacts{position:absolute;left:300px;top:94px;list-style:none;font-family:'Oswald',sans-serif;font-size:11.5px;color:var(--ink-gray);letter-spacing:.04em}
  .contacts li{display:flex;align-items:center;height:25px}
  .contacts svg{width:17px;height:17px;margin-right:10px;flex:none}
</style>
</head>
<body>
<main class="canvas">

  <section class="card card--back" aria-label="Card back with brand and tagline">
    <svg class="card__art" viewBox="0 0 560 320" preserveAspectRatio="none" aria-hidden="true">
      <polygon points="0,262 560,232 560,320 0,320" fill="var(--blue-light)"/>
      <polygon points="0,280 560,258 560,320 0,320" fill="var(--blue-deep)"/>
    </svg>
    <p class="brand">KT4 LINKWAY</p>
    <p class="tagline">bringing each brand closer to the right crowd</p>
  </section>

  <section class="card card--front" aria-label="Card front with contact details">
    <svg class="card__art" viewBox="0 0 560 320" preserveAspectRatio="none" aria-hidden="true">
      <polygon points="0,232 560,262 560,320 0,320" fill="var(--blue-light)"/>
      <polygon points="0,258 560,280 560,320 0,320" fill="var(--blue-deep)"/>
    </svg>
    <p class="brand">KT4 LINKWAY</p>
    <div class="person">
      <p class="person__name">DANA MORRELL</p>
      <p class="person__title">TITLE</p>
    </div>
    <span class="divider"></span>
    <ul class="contacts">
      <li><svg viewBox="0 0 20 20"><circle cx="10" cy="10" r="10" fill="#5ab0e0"/><path d="M7 5.5l1.6 2.4-1 1.1c.6 1.3 1.5 2.2 2.8 2.8l1.1-1 2.4 1.6-.8 1.6c-3.4.2-7.3-3.7-7.1-7.1z" fill="#fff"/></svg>012-555-480</li>
      <li><svg viewBox="0 0 20 20"><rect x="1" y="4" width="18" height="12" rx="1.5" fill="#5ab0e0"/><path d="M2 5l8 6 8-6" fill="none" stroke="#fff" stroke-width="1.4"/></svg>DANA@KT4LINKWAY.COM</li>
      <li><svg viewBox="0 0 20 20"><circle cx="10" cy="10" r="9" fill="#5ab0e0"/><g fill="none" stroke="#fff" stroke-width="1.1"><ellipse cx="10" cy="10" rx="3.6" ry="8"/><path d="M2 10h16M3.5 6h13M3.5 14h13"/></g></svg>WWW.KT4LINKWAY.COM</li>
    </ul>
  </section>

</main>
</body>
</html>
```